Chinese Language Posters - TKUOME

We have created a series of African American heritage posters that will be distributed to Chinese Language Schools. We need a designer to create great posters for K-12 programs.

Quotes:
We have quotes from 6 important figures in Black History. We are seeking a designer to develop a poster utilizing at least one quote from each historical figure.

The designer MUST be fluent in Chinese in order to ensure the appropriate type and font.

Our organization, Tidewater Kestrel Union of Orchard Mentors Exchange, is a small organization of parents in the Bay Area working to encourage and support Black students learning the Chinese language.

Target Market(s)

These posters will be made available to Chinese Immersion schools (k-12).

Industry/Entity Type

Learning

Requirements
Must have
• Each poster should contain one quote from the list below.

Please create a poster of one historical figure and include their quote. The image can be abstract, landscape or an image of the figure.

The image should also include our logo. Our preferred logo is with the puffs but we understand if the clipart logo may be a better fit for the posters. (We LOVE the puffs logo though).
Nice to have
• I have uploaded images of each figure. The images can be used or a more abstract background. We are flexible. We would prefer a mix that includes figures and abstract backgrounds just focusing on the quote. We are open.

```html
<!DOCTYPE html>
<html lang="en">
<head>
<meta charset="utf-8">
<title>TKUOME Poster Design</title>
<link rel="stylesheet" href="https://fonts.googleapis.com/css2?family=Libre+Baskerville&family=Noto+Serif+SC:wght@700;900&display=swap">
<style>
  :root {
    --page: #ffffff;
    --ink: #333333;
    --tab: #4a4a4a;
    --tab-text: #ffffff;
    --green: #6cb52a;
    --orange: #e0661e;
    --yellow: #f4ec2c;
    --quote-shadow: #1f5a12;
    --red: #d8261e;
    --gold: #f0d030;
    --badge: #ffffff;
    --badge-ink: #1a1a1a;
  }
  * { margin: 0; padding: 0; box-sizing: border-box; }
  html, body { width: 1200px; height: 848px; overflow: hidden; background: var(--page); }
  .sheet { position: relative; width: 1200px; height: 848px; font-family: "Libre Baskerville", Georgia, serif; color: var(--ink); }

  .sheet-tab {
    position: absolute; left: 876px; top: 40px; width: 324px; height: 47px;
    background: var(--tab); color: var(--tab-text);
    font-size: 20px; line-height: 47px; text-align: center;
  }
  .sheet-title {
    position: absolute; left: 442px; top: 122px; width: 310px;
    font-size: 19px; text-align: center; padding-bottom: 4px;
    border-bottom: 1px solid var(--ink);
  }

  .poster { position: absolute; top: 220px; width: 350px; height: 493px; overflow: hidden; }
  .poster--one { left: 31px; }
  .poster--two { left: 422px; }
  .poster--three { left: 805px; }
  .poster svg { position: absolute; inset: 0; }

  .quote {
    position: absolute; left: 0; right: 0; top: 250px;
    font-family: "Noto Serif SC", serif; font-weight: 900;
    text-align: center; color: var(--yellow);
    text-shadow: 2px 2px 0 var(--quote-shadow);
  }
  .quote span { display: block; }
  .quote-lead { font-size: 17px; line-height: 24px; color: #1d2a10; text-shadow: 1px 1px 0 var(--yellow), -1px 0 0 var(--yellow); }
  .quote-line { font-size: 31px; line-height: 46px; letter-spacing: 7px; }
  .quote-line--first { margin-top: 8px; margin-left: -8px; }
  .quote-end { font-size: 42px; line-height: 56px; }
  .poster--three .quote { color: var(--red); text-shadow: 2px 2px 0 var(--gold); }
  .poster--three .quote-lead { color: var(--red); text-shadow: 1px 1px 0 var(--gold); }

  .org-badge {
    position: absolute; left: 278px; top: 420px; width: 64px; height: 68px;
    background: var(--badge); display: flex; flex-direction: column;
    align-items: center; justify-content: center; gap: 6px;
    font-family: "Noto Serif SC", serif; font-weight: 700; font-size: 11px; color: var(--badge-ink);
  }
  .org-badge i { width: 16px; height: 16px; background: var(--red); display: block; }

  .poster-label { position: absolute; top: 733px; width: 350px; text-align: center; font-size: 19px; }
</style>
</head>
<body>
<main class="sheet">
  <div class="sheet-tab">TKUOME Poster Design</div>
  <h1 class="sheet-title" style="font-weight:400">TKUOME Poster ( Marcus Hale )</h1>

  <section class="poster poster--one">
    <svg width="350" height="493" viewBox="0 0 350 493">
      <defs>
        <linearGradient id="photo-warm" x1="0" y1="0" x2="0" y2="1">
          <stop offset="0" stop-color="#2a1f18"/>
          <stop offset="0.35" stop-color="#6b4a3c"/>
          <stop offset="1" stop-color="#e3aca0"/>
        </linearGradient>
      </defs>
      <rect width="350" height="493" fill="url(#photo-warm)" role="img" aria-label="Photograph of a smiling man in glasses and a suit at a microphone, warm tint"/>
      <polygon points="290,0 350,0 350,140 250,320 225,320" fill="#d8c84a" opacity="0.35"/>
      <polygon points="0,340 180,493 0,493" fill="var(--green)"/>
      <polygon points="350,320 350,493 180,493" fill="var(--green)"/>
    </svg>
    <div class="quote">
      <span class="quote-lead">教育是我们通往未来的护照, 因为</span>
      <span class="quote-line quote-line--first">明天属于那些在今</span>
      <span class="quote-line">天为其做好</span>
      <span class="quote-line">准备的</span>
      <span class="quote-end">人</span>
    </div>
    <div class="org-badge"><i></i>TKUOME</div>
  </section>

  <section class="poster poster--two">
    <svg width="350" height="493" viewBox="0 0 350 493">
      <defs>
        <linearGradient id="photo-mono" x1="0" y1="0" x2="0" y2="1">
          <stop offset="0" stop-color="#1d1414"/>
          <stop offset="0.35" stop-color="#5a5050"/>
          <stop offset="1" stop-color="#c9c9c9"/>
        </linearGradient>
      </defs>
      <rect width="350" height="493" fill="url(#photo-mono)" role="img" aria-label="Black and white photograph of a smiling man in glasses and a suit at a microphone, red-tinted backdrop"/>
      <polygon points="290,0 350,0 350,140 250,320 225,320" fill="#c8b040" opacity="0.3"/>
      <polygon points="0,340 180,493 0,493" fill="var(--orange)"/>
      <polygon points="350,320 350,493 180,493" fill="var(--orange)"/>
    </svg>
    <div class="quote">
      <span class="quote-lead">教育是我们通往未来的护照, 因为</span>
      <span class="quote-line quote-line--first">明天属于那些在今</span>
      <span class="quote-line">天为其做好</span>
      <span class="quote-line">准备的</span>
      <span class="quote-end">人</span>
    </div>
    <div class="org-badge"><i></i>TKUOME</div>
  </section>

  <section class="poster poster--three">
    <svg width="350" height="493" viewBox="0 0 350 493">
      <defs>
        <linearGradient id="photo-grey" x1="0" y1="0" x2="0" y2="1">
          <stop offset="0" stop-color="#6e6e6e"/>
          <stop offset="0.4" stop-color="#9a9a9a"/>
          <stop offset="1" stop-color="#d4d4d4"/>
        </linearGradient>
      </defs>
      <rect width="350" height="493" fill="url(#photo-grey)" role="img" aria-label="Grey photograph of a smiling man in glasses and a suit at a microphone"/>
      <polygon points="290,0 350,0 350,140 250,320 225,320" fill="#ffffff" opacity="0.3"/>
    </svg>
    <div class="quote">
      <span class="quote-lead">教育是我们通往未来的护照, 因为</span>
      <span class="quote-line quote-line--first">明天属于那些在今</span>
      <span class="quote-line">天为其做好</span>
      <span class="quote-line">准备的</span>
      <span class="quote-end">人</span>
    </div>
    <div class="org-badge"><i></i>TKUOME</div>
  </section>

  <p class="poster-label" style="left:31px">Poster Design 1</p>
  <p class="poster-label" style="left:422px">Poster Design 2</p>
  <p class="poster-label" style="left:805px">Poster Design 3</p>
</main>
</body>
</html>
```